Carrier needs an Amazing Flyer

Our business is needing a corporate flyer. At the moment we transport different products, some of them clasified as hazardous, through out center and south Peru-South America. We would like the flyer to comunicate punctuality, safety and profesionalism. Our corporate colors are green (C=85,M=25,Y=55,K=10) and black. At the moment, we are developing what the flyer should say (we will upload it later), but the flyer should have 04 parts: Clients, Vehicles, Services and Routes.

The information to every part is the following:

Clients: the ones listed in our webpage (www.cargavelorumbo.pe), which you can find in the option "Clientes". We add the text of this part in uploaded files with a .doc extension.

Vehicles: the ones listed in our webpage (www.cargavelorumbo.pe), which you can find in the option "Flota". We add the text of this part in uploaded files with a .doc extension.

Services: the ones listed in our webpage (www.cargavelorumbo.pe), which you can find in the option "Servicios". We add the text of this part in uploaded files with a .doc extension. The smart art is only a example. We would like too see more ideas but use the smart art as an example.

Routes: At the moment we are covering all South of Peru and his capital city, Lima. Thefore, we are transporting between cities around the mentioned area. An idea to show this can be a map of those Peru areas. We will like to receive more ideas about this. In order to help you draw the map, the cities adn towns that we most cover are: Lima, Pisco, Ica, Nasca, Chala, Atico, OcoƱa, Camana, Pedregal, Majes, Mollendo, Matarani, Ilo, Moquegua, Cocachacra, Tacna, Arequipa, Juliaca, Puno, Ilave, Desaguadero, Cusco, Sicuani, Chivay, Imata, Santa Lucia, Ayaviri, Puerto Maldonado, Macusani, Mazuco, Espinar. You can use google maps, to have an idea of where these cities and towns are. Any question just write us a message.

Target Market(s)

Other Business

Industry/Entity Type

Business

Requirements
Must have
• We are willing to print the flyer in a A4 format and bent it in two. Also, we will use the flyer as a digital presentation to send it to our clients by email. All the text in the flyer must be in spanish. For those who do not know the language, we will guide you. We don't want to many words in the flyer.
Nice to have
• We would like to see something that captures the attention of the reader, so he or she give it some minutes to check it out. Therefore, the parts should be strategically located.
Should not have
• Don't put in a map of South America. We are not transporting outside of Peru at the moment. This might give a wrong impression to new customers.

```html
<!DOCTYPE html>
<html lang="es">
<head>
<meta charset="utf-8">
<title>Transportes Velorumbo Sur – Folleto corporativo</title>
<link href="https://fonts.googleapis.com/css2?family=Fira+Sans:ital,wght@0,400;0,500;0,700;1,700&display=swap" rel="stylesheet">
<style>
  :root{
    --teal:#128a7b;
    --teal-deep:#0c6c60;
    --teal-soft:#2f8f82;
    --yellow:#ffd400;
    --yellow-olive:#c9bd3a;
    --black:#060606;
    --white:#ffffff;
    --paper:#e9e6e1;
  }
  *{margin:0;padding:0;box-sizing:border-box}
  html,body{width:1200px;height:1200px;overflow:hidden}
  body{background:var(--paper);font-family:"Fira Sans",sans-serif;position:relative}
  .spread{position:absolute;left:205px;width:988px;height:699px;transform:scale(0.8);transform-origin:0 0;background:var(--black);overflow:hidden}
  .spread--services{top:29px}
  .spread--clients{top:612px}
  .spread svg.art{position:absolute;inset:0;width:988px;height:699px}
  .section-tag{position:absolute;width:200px;height:40px}
  .section-tag text{font-family:"Fira Sans",sans-serif;font-weight:700;font-style:italic;font-size:17px}
  .body-copy{position:absolute;width:406px;font-size:12.6px;line-height:17px;font-weight:500;color:var(--white);letter-spacing:-0.1px}
  .brand{position:absolute;display:flex;align-items:center;gap:10px}
  .brand__mark{width:34px;height:34px;border-radius:50%;background:var(--teal)}
  .brand__name{font-family:"Fira Sans",sans-serif;font-weight:700;font-size:19px;line-height:20px;color:var(--black)}
</style>
</head>
<body>

<section class="spread spread--services">
  <svg class="art" viewBox="0 0 988 699" xmlns="http://www.w3.org/2000/svg">
    <defs>
      <radialGradient id="mapTone" cx="50%" cy="45%" r="60%">
        <stop offset="0" stop-color="#e4e3df"/>
        <stop offset="0.55" stop-color="#c9c8c3"/>
        <stop offset="1" stop-color="#c9c8c3" stop-opacity="0"/>
      </radialGradient>
      <linearGradient id="truckWhite" x1="0" y1="0" x2="1" y2="1">
        <stop offset="0" stop-color="#6f7f8c"/>
        <stop offset="0.45" stop-color="#e6e8ea"/>
        <stop offset="1" stop-color="#9a6a50"/>
      </linearGradient>
      <linearGradient id="tealPhoto" x1="0" y1="0" x2="1" y2="1">
        <stop offset="0" stop-color="var(--teal-soft)"/>
        <stop offset="1" stop-color="var(--teal)"/>
      </linearGradient>
    </defs>
    <!-- left page -->
    <rect x="0" y="0" width="494" height="699" fill="var(--black)"/>
    <path d="M0,334 L494,579 V699 H0 Z" fill="url(#tealPhoto)" role="img" aria-label="Foto tenue de camión volquete tras tinte verde"/>
    <ellipse cx="330" cy="370" rx="210" ry="200" fill="url(#mapTone)" role="img" aria-label="Mapa de las regiones del sur del Perú"/>
    <path d="M0,583 H255 L300,699 H0 Z" fill="var(--white)"/>
    <!-- right page -->
    <rect x="494" y="0" width="494" height="699" fill="var(--black)"/>
    <path d="M494,0 H988 V240 C988,292 952,306 905,296 L494,128 Z" fill="var(--yellow)"/>
    <path d="M700,0 H988 V240 C988,292 952,306 905,296 L760,236 Z" fill="var(--yellow-olive)" opacity="0.35"/>
    <path d="M540,215 L988,352 V699 H860 L494,545 V300 Z" fill="url(#truckWhite)" role="img" aria-label="Foto de tractocamión blanco frente a muro de ladrillo"/>
    <path d="M494,545 L870,699 H494 Z" fill="var(--teal)"/>
    <path d="M494,699 V684 C494,646 540,628 600,634 L760,682 V699 Z" fill="var(--yellow)"/>
  </svg>

  <svg class="section-tag" style="left:0;top:29px" viewBox="0 0 200 40">
    <polygon points="0,0 122,0 132,20 122,40 0,40" fill="var(--teal)"/>
    <g fill="var(--teal)">
      <polygon points="134,0 146,0 160,20 146,40 134,40 148,20"/>
      <polygon points="154,0 166,0 180,20 166,40 154,40 168,20"/>
      <polygon points="174,0 186,0 200,20 186,40 174,40 188,20"/>
    </g>
    <text x="28" y="26" fill="var(--yellow)">Servicios</text>
  </svg>

  <p class="body-copy" style="left:28px;top:89px">La “Superación” es uno de los valores pilares de nuestra organi&shy;zación. Es por eso que desde nuestra fundación a la fecha venimos incrementando la cantidad de servicios que brindamos, con el objetivo de adecuarnos a las necesidades de nuestros clientes. A la fecha los servicios que brindamos son:</p>

  <div class="brand" style="left:32px;top:622px">
    <span class="brand__mark"></span>
    <span class="brand__name">Transportes<br>Velorumbo Sur</span>
  </div>
  <div class="brand" style="left:548px;top:40px">
    <span class="brand__mark"></span>
    <span class="brand__name">Transportes<br>Velorumbo Sur</span>
  </div>
</section>

<section class="spread spread--clients">
  <svg class="art" viewBox="0 0 988 699" xmlns="http://www.w3.org/2000/svg">
    <defs>
      <linearGradient id="dumpTruck" x1="0" y1="0" x2="0" y2="1">
        <stop offset="0" stop-color="#8fa6bd"/>
        <stop offset="0.45" stop-color="#dcdcd8"/>
        <stop offset="1" stop-color="#b3a590"/>
      </linearGradient>
      <linearGradient id="teamPhoto" x1="0" y1="0" x2="0" y2="1">
        <stop offset="0" stop-color="#d9d9d6"/>
        <stop offset="0.45" stop-color="#a0563f"/>
        <stop offset="1" stop-color="#c2b29c"/>
      </linearGradient>
      <linearGradient id="tealTruck" x1="0" y1="0" x2="1" y2="1">
        <stop offset="0" stop-color="var(--teal-soft)"/>
        <stop offset="1" stop-color="var(--teal)"/>
      </linearGradient>
    </defs>
    <!-- left page -->
    <rect x="0" y="0" width="494" height="699" fill="var(--black)"/>
    <path d="M0,0 H175 L494,118 V385 C494,428 470,438 430,425 L0,305 Z" fill="var(--teal)"/>
    <path d="M0,327 L494,442 V699 H0 Z" fill="url(#dumpTruck)" role="img" aria-label="Foto de camión volquete blanco en obra"/>
    <!-- right page -->
    <rect x="494" y="0" width="494" height="699" fill="var(--black)"/>
    <path d="M494,0 H988 V338 L494,140 Z" fill="url(#teamPhoto)" role="img" aria-label="Foto grupal del equipo frente a la sede"/>
    <path d="M494,290 C494,240 532,220 592,226 L988,346 V699 H494 Z" fill="url(#tealTruck)" role="img" aria-label="Foto tenue de camión tras tinte verde"/>
  </svg>

  <svg class="section-tag" style="left:0;top:123px" viewBox="0 0 200 40">
    <polygon points="0,0 122,0 132,20 122,40 0,40" fill="var(--yellow)"/>
    <g fill="var(--yellow)">
      <polygon points="134,0 146,0 160,20 146,40 134,40 148,20"/>
      <polygon points="154,0 166,0 180,20 166,40 154,40 168,20"/>
      <polygon points="174,0 186,0 200,20 186,40 174,40 188,20"/>
    </g>
    <text x="28" y="26" fill="var(--black)">Clientes</text>
  </svg>

  <p class="body-copy" style="left:28px;top:174px">La “Superación” es uno de los valores pilares de nuestra organi&shy;zación. Es por eso que desde nuestra fundación a la fecha venimos incrementando la cantidad de servicios que brindamos, con el objetivo de adecuarnos a las necesidades de nuestros clientes. A la fecha los servicios que brindamos son:</p>

  <svg class="section-tag" style="left:494px;top:431px" viewBox="0 0 200 40">
    <polygon points="0,0 122,0 132,20 122,40 0,40" fill="var(--yellow)"/>
    <g fill="var(--yellow)">
      <polygon points="134,0 146,0 160,20 146,40 134,40 148,20"/>
      <polygon points="154,0 166,0 180,20 166,40 154,40 168,20"/>
      <polygon points="174,0 186,0 200,20 186,40 174,40 188,20"/>
    </g>
    <text x="28" y="26" fill="var(--black)">Flota</text>
  </svg>

  <p class="body-copy" style="left:522px;top:482px">Es nuestra preocupación contar con unidades en excelente estado, que nos permitan realizar nuestras operaciones sin interrupciones por mantenimientos no planificados. Por tal motivo es que conta&shy;mos una flota de unidades moderna. La cual describimos a continuación:</p>
</section>

</body>
</html>
```